Modern, Sleek Business Card Design for Corvane Systems

Please create a modern business card, preferably all black with white logo and writing for Corvane Systems, a defense and aerospace company.

Contact Information for Business Card

symbol on one side and name, title, contact info on the other side.

```html
<!DOCTYPE html>
<html lang="en">
<head>
<meta charset="utf-8">
<title>Corvane Systems Business Card</title>
<link href="https://fonts.googleapis.com/css2?family=Lato:wght@400;700&display=swap" rel="stylesheet">
<style>
  :root {
    --backdrop: #3b3b3b;
    --card-dark: #050505;
    --card-light: #ffffff;
    --ink-light: #ffffff;
    --ink-dark: #111111;
    --rule: #1a1a1a;
  }
  * { margin: 0; padding: 0; box-sizing: border-box; }
  html, body { width: 1200px; height: 694px; overflow: hidden; }
  body {
    background: var(--backdrop);
    font-family: "Lato", sans-serif;
    position: relative;
  }
  .card {
    position: absolute;
    top: 204px;
    width: 500px;
    height: 286px;
    border-radius: 22px;
    overflow: hidden;
  }
  .card-front { left: 60px; background: var(--card-dark); }
  .card-back { left: 640px; background: var(--card-light); color: var(--ink-dark); }

  .front-brand {
    position: absolute;
    inset: 0;
    display: flex;
    flex-direction: column;
    align-items: center;
    justify-content: center;
    gap: 18px;
  }
  .front-brand .brand-square {
    width: 46px; height: 46px;
    background: var(--ink-light);
  }
  .front-brand .brand-name {
    color: var(--ink-light);
    font-weight: 700;
    font-size: 40px;
    letter-spacing: 4px;
    text-transform: uppercase;
  }

  .back-brand {
    position: absolute;
    top: 40px;
    right: 34px;
    display: flex;
    align-items: center;
    gap: 12px;
  }
  .back-brand .brand-square { width: 26px; height: 26px; background: var(--ink-dark); }
  .back-brand .brand-name {
    font-weight: 700;
    font-size: 24px;
    letter-spacing: 2px;
    text-transform: uppercase;
  }

  .holder {
    position: absolute;
    left: 34px;
    top: 150px;
  }
  .holder-name { font-weight: 700; font-size: 21px; }
  .holder-title { font-weight: 400; font-size: 14px; margin-top: 2px; }

  .divider {
    position: absolute;
    left: 34px;
    right: 34px;
    top: 200px;
    height: 1px;
    background: var(--rule);
  }

  .address {
    position: absolute;
    right: 34px;
    top: 214px;
    text-align: right;
    font-size: 14px;
    line-height: 1.45;
    font-style: normal;
  }

  .contacts {
    position: absolute;
    left: 34px;
    top: 212px;
    list-style: none;
    font-size: 13px;
  }
  .contacts li {
    display: flex;
    align-items: center;
    gap: 10px;
    height: 20px;
  }
  .contacts svg { width: 13px; height: 13px; fill: var(--ink-dark); }
</style>
</head>
<body>
  <section class="card card-front">
    <div class="front-brand">
      <span class="brand-square"></span>
      <span class="brand-name">Corvane Systems</span>
    </div>
  </section>

  <section class="card card-back">
    <div class="back-brand">
      <span class="brand-square"></span>
      <span class="brand-name">Corvane Systems</span>
    </div>

    <div class="holder">
      <p class="holder-name">Marcus Hale</p>
      <p class="holder-title">Owner</p>
    </div>

    <div class="divider"></div>

    <ul class="contacts">
      <li>
        <svg viewBox="0 0 16 16" aria-hidden="true"><path d="M3.6 1.5l2.3 2.3-1.3 1.9c.9 2 2.6 3.6 4.6 4.6l1.9-1.3 2.3 2.3-1.6 2.2C6.6 13.3 2.7 9.4 1.5 3.2z"/></svg>
        <span>055-210 384 617</span>
      </li>
      <li>
        <svg viewBox="0 0 16 16" aria-hidden="true"><path d="M1 3h14v10H1z M1 3l7 6 7-6" stroke="#fff" stroke-width="1"/></svg>
        <span>info@corvane.com</span>
      </li>
      <li>
        <svg viewBox="0 0 16 16" aria-hidden="true"><circle cx="8" cy="8" r="7"/><path d="M1 8h14M8 1c-3 3-3 11 0 14M8 1c3 3 3 11 0 14" stroke="#fff" stroke-width="1" fill="none"/></svg>
        <span>www.corvanesys.com</span>
      </li>
    </ul>

    <address class="address">
      318, Halden Ridge Avenue<br>
      60817, Northland
    </address>
  </section>
</body>
</html>
```